My Insurance Agency - R. T. Palloway Insurance Services Provides Insurance products to all of California. Most specifically the Bay Area.
"The Coverage Guy" is who I am advertising. providing Insurance solutions and consultations.
My Main Products are:
Life
Health
Disability
Accident
Employee Benefits
The colors of the card should match my uploaded logo.
I want the card to portray professionalism and security....Trust...and make people want to pick up the phone right now and make an appointment?
Target Market(s)
Young families, Seniors
Industry/Entity Type
Insurance
Look and feel
Each slider illustrates characteristics of the customer's brand and the style your logo design should communicate.

```html
<!DOCTYPE html>
<html lang="en">
<head>
<meta charset="utf-8">
<title>The Coverage Guy – Postcard</title>
<link rel="stylesheet" href="https://fonts.googleapis.com/css2?family=Cinzel:wght@600;700&family=Source+Sans+3:ital,wght@0,400;0,600;0,700;1,400&display=swap">
<style>
  :root {
    --page-bg: #e8e6e2;
    --card-border-light: #8fadd8;
    --card-white: #ffffff;
    --ink-navy: #2e3563;
    --brand-red: #e2262b;
    --frame-navy: #1b2850;
    --photo-light: #647f9e;
    --photo-mid: #3b5172;
    --photo-dark: #1d2a44;
    --suit-dark: #1a2338;
    --suit-mid: #2b3852;
    --suit-light: #3d4b66;
    --highlight: rgba(225, 228, 234, 0.55);
    --headline-blue: #86c9ef;
    --tick-blue: #7fc0ea;
    --white: #ffffff;
    --rule: #2b2b2b;
  }
  * { margin: 0; padding: 0; box-sizing: border-box; }
  html, body { width: 1200px; height: 904px; overflow: hidden; }
  body {
    background: var(--page-bg);
    position: relative;
    font-family: "Source Sans 3", sans-serif;
  }

  .postcard {
    position: absolute;
    top: 237px;
    width: 570px;
    height: 430px;
  }

  /* ---------- Address side ---------- */
  .postcard--back {
    left: 20px;
    background: var(--card-border-light);
    padding: 16px;
  }
  .back-face {
    position: relative;
    width: 100%;
    height: 100%;
    background: var(--card-white);
  }
  .brand-mark {
    position: absolute;
    display: flex;
    align-items: center;
    gap: 6px;
    z-index: 2;
  }
  .brand-mark__dot {
    width: 14px; height: 14px; border-radius: 50%;
    flex: none;
  }
  .brand-mark__name {
    font-family: "Source Sans 3", sans-serif;
    font-weight: 600;
    font-size: 13px;
    line-height: 1.1;
    text-transform: uppercase;
    letter-spacing: 0.5px;
  }
  .back-face .brand-mark { left: 14px; top: 16px; width: 100px; }
  .back-face .brand-mark__dot { background: var(--ink-navy); }
  .back-face .brand-mark__name { color: var(--ink-navy); }

  .back-phone {
    position: absolute;
    left: 123px; top: 8px;
    font-weight: 700;
    font-size: 31px;
    color: var(--brand-red);
    letter-spacing: -0.3px;
  }
  .stamp-box {
    position: absolute;
    left: 435px; top: 4px;
    width: 86px; height: 112px;
    border: 2px solid var(--rule);
    display: flex; align-items: center; justify-content: center;
    font-size: 12px; letter-spacing: 0.5px; color: #222;
  }
  .message {
    position: absolute;
    left: 8px; top: 84px;
    width: 250px;
    font-style: italic;
    font-size: 14.5px;
    line-height: 18.5px;
    color: var(--ink-navy);
    white-space: nowrap;
  }
  .message p { margin-bottom: 18.5px; }
  .message .indent { padding-left: 9px; }
  .message p.tight { margin-bottom: 0; }
  .signature {
    position: absolute;
    left: 8px; top: 361px;
    color: var(--brand-red);
  }
  .signature__company { font-size: 15px; font-weight: 600; line-height: 19px; }
  .signature__region { font-size: 12.5px; line-height: 17px; }
  .divider {
    position: absolute;
    left: 268px; top: 112px;
    width: 2px; height: 251px;
    background: var(--rule);
  }
  .address-line {
    position: absolute;
    left: 286px;
    width: 242px; height: 1.5px;
    background: var(--rule);
  }
  .address-line--1 { top: 175px; }
  .address-line--2 { top: 237px; }
  .address-line--3 { top: 300px; }

  /* ---------- Picture side ---------- */
  .postcard--front {
    left: 610px;
    background: var(--frame-navy);
    padding: 15px 20px 10px 19px;
  }
  .front-face {
    position: relative;
    width: 100%;
    height: 100%;
    overflow: hidden;
    background: linear-gradient(100deg, var(--photo-light) 0%, var(--photo-mid) 45%, var(--photo-dark) 100%);
  }
  .hero-photo {
    position: absolute;
    left: 205px; top: 0; right: 0; bottom: 0;
    border-top-left-radius: 140px 200px;
    background:
      radial-gradient(ellipse 22% 26% at 66% 60%, var(--highlight) 0%, rgba(225,228,234,0) 100%),
      radial-gradient(ellipse 40% 18% at 58% 40%, rgba(220,200,190,0.35) 0%, rgba(220,200,190,0) 100%),
      radial-gradient(ellipse 40% 16% at 66% 86%, rgba(220,200,190,0.3) 0%, rgba(220,200,190,0) 100%),
      linear-gradient(90deg, var(--suit-light) 0%, var(--suit-mid) 35%, var(--suit-dark) 100%);
  }
  .front-face .brand-mark { left: 8px; top: 10px; width: 92px; }
  .front-face .brand-mark__dot { background: var(--white); }
  .front-face .brand-mark__name { color: var(--white); font-size: 12px; }

  .headline {
    position: absolute;
    left: 106px; top: 35px;
    font-family: "Cinzel", serif;
    font-weight: 700;
    font-size: 15.5px;
    letter-spacing: 0.6px;
    text-transform: uppercase;
    color: var(--headline-blue);
    white-space: nowrap;
    z-index: 2;
  }
  .product-list {
    position: absolute;
    left: 6px; top: 140px;
    list-style: none;
    z-index: 2;
  }
  .product-list li {
    display: flex; align-items: center; gap: 7px;
    height: 31px;
    font-family: "Cinzel", serif;
    font-weight: 700;
    font-size: 17px;
    color: var(--white);
    letter-spacing: 0.3px;
  }
  .product-list svg { width: 11px; height: 11px; flex: none; }
  .front-phone {
    position: absolute;
    left: 7px; top: 350px;
    font-weight: 600;
    font-size: 33px;
    color: var(--white);
    letter-spacing: -0.2px;
    z-index: 2;
  }
</style>
</head>
<body>

  <section class="postcard postcard--back" aria-label="Postcard address side">
    <div class="back-face">
      <div class="brand-mark">
        <span class="brand-mark__dot"></span>
        <span class="brand-mark__name">The Coverage Guy</span>
      </div>
      <div class="back-phone">(916)555-0142</div>
      <div class="stamp-box">STAMP</div>

      <div class="message">
        <p><span class="indent">Bad things happen to good people, but</span><br>a good insurance policy can keep them<br>from becoming devastating.</p>
        <p><span class="indent">Your protection is our priority. We</span><br>promise to stay on top of your changing<br>insurance needs, process your claims<br>promptly, and respond to all enquiries<br>with the urgency they deserve.</p>
        <p class="tight"><span class="indent">Think of us as your insurance</span><br>bodyguards, looking out for you now and<br>in the future.<br>Sincerely,</p>
      </div>

      <div class="signature">
        <div class="signature__company">R. T. Palloway Insurance Services,</div>
        <div class="signature__region">California, the Bay Area</div>
      </div>

      <div class="divider"></div>
      <div class="address-line address-line--1"></div>
      <div class="address-line address-line--2"></div>
      <div class="address-line address-line--3"></div>
    </div>
  </section>

  <section class="postcard postcard--front" aria-label="Postcard picture side">
    <div class="front-face">
      <div class="hero-photo" role="img" aria-label="Photo of a man in a dark suit holding his hands protectively around a paper cut-out of a family"></div>

      <div class="brand-mark">
        <span class="brand-mark__dot"></span>
        <span class="brand-mark__name">The Coverage Guy</span>
      </div>
      <h1 class="headline">Your Protection is Our Priority</h1>

      <ul class="product-list">
        <li><svg viewBox="0 0 12 12"><path d="M1 6 L4.5 10.5 L11 1" fill="none" stroke="var(--tick-blue)" stroke-width="1.6"/></svg>Life</li>
        <li><svg viewBox="0 0 12 12"><path d="M1 6 L4.5 10.5 L11 1" fill="none" stroke="var(--tick-blue)" stroke-width="1.6"/></svg>Health</li>
        <li><svg viewBox="0 0 12 12"><path d="M1 6 L4.5 10.5 L11 1" fill="none" stroke="var(--tick-blue)" stroke-width="1.6"/></svg>Disability</li>
        <li><svg viewBox="0 0 12 12"><path d="M1 6 L4.5 10.5 L11 1" fill="none" stroke="var(--tick-blue)" stroke-width="1.6"/></svg>Accident</li>
        <li><svg viewBox="0 0 12 12"><path d="M1 6 L4.5 10.5 L11 1" fill="none" stroke="var(--tick-blue)" stroke-width="1.6"/></svg>Employee Benefits</li>
      </ul>

      <div class="front-phone">(916)555-0142</div>
    </div>
  </section>

</body>
</html>
```